Design Fresh and modern brochure about hypnosis

We need a clean and modern brochure designed for our hypnosis center. I have text, a logo, and a single image. I'd like all placed in a tri-fold brochure with design elements added and I'd like the result in a format which can be modified, like InDesign. The brochure should appear modern and clean, but also with a softer look to appear compassionate. The company values are professional, compassionate, and local. Local is the Pacific Northwest. Colors should match the logo, blue with elements of water. I'd like to see shades of blue with white.
Updates

Hello designers. Thank you all for your great brochure designs thus far. 

At this time I've narrowed down the top 2 designs and those designers have been contacted. 

So right now, any new designs would be in consideration for third place. I want to be fair to your time, so please consider if you're still interested in submitting a design for 3rd place or not. 

Thank you. 

Target Market(s)

Adults in western US who want to improve their lives. Primarily 30+ in age, english speaking, and working full or part time.

Industry/Entity Type

It Company

Colors
85cae6
0555a3
3276b5
86cfc6
32b7a4

Requirements
Must have
• The brochure must include the logo and image attached, and should fit in the tri-fold design, similar to the example brochure. It also needs to be in a format that can be easily modified over time, as I typically change text in the brochure. InDesign would be great.
Nice to have
• Additional design elements - like areas for a call-out to highlight features.

```html
<!DOCTYPE html>
<html lang="en">
<head>
<meta charset="utf-8">
<title>Harbor Mist Hypnosis Center – Tri-fold Brochure</title>
<link href="https://fonts.googleapis.com/css2?family=Open+Sans:wght@400;600;700&family=Tinos:wght@400;700&display=swap" rel="stylesheet">
<style>
  :root{
    --sky:#85cae6;
    --deep:#0555a3;
    --mid:#3276b5;
    --sea:#86cfc6;
    --teal:#32b7a4;
    --ink:#1f2d3a;
    --paper:#ffffff;
    --stage:#e6e7e9;
    --accent-red:#a3202a;
  }
  *{box-sizing:border-box;margin:0;padding:0}
  html,body{width:1200px;height:502px;overflow:hidden;background:var(--stage)}
  .canvas{position:relative;width:1200px;height:502px}
  .spread{position:absolute;top:27px;width:580px;height:448px;display:flex;background:var(--paper);box-shadow:0 4px 14px rgba(0,0,0,.18);overflow:hidden}
  .spread--outside{left:10px}
  .spread--inside{left:610px}
  .panel{position:relative;width:33.333%;height:100%;overflow:hidden}

  /* soft water-tone areas standing in for the decorative artwork */
  .water-area{position:absolute;left:0;right:0}
  .water-area--intro{bottom:0;height:150px;background:linear-gradient(180deg,rgba(255,255,255,0),rgba(255,255,255,.16))}
  .water-area--services{top:238px;height:70px;background:linear-gradient(180deg,rgba(133,202,230,0),rgba(133,202,230,.3),rgba(133,202,230,0))}
  .water-area--cover{top:262px;height:70px;background:linear-gradient(180deg,rgba(133,202,230,0),rgba(134,207,198,.28),rgba(133,202,230,0))}

  /* outside */
  .panel--intro{background:linear-gradient(160deg,var(--deep),var(--mid) 55%,var(--sky));color:#fff;padding:22px 14px;font-family:"Open Sans",sans-serif}
  .intro__title{position:relative;font-size:11px;font-weight:700;line-height:1.3;margin-bottom:10px}
  .intro__text{position:relative;font-size:7.4px;line-height:1.55}
  .intro__text p{margin-bottom:7px}

  .panel--services{background:var(--paper);font-family:"Open Sans",sans-serif;color:var(--ink);padding:20px 12px}
  .services__title{position:relative;font-size:9.5px;font-weight:700;line-height:1.3;margin-bottom:8px;color:var(--deep)}
  .services__list{position:relative;display:grid;grid-template-columns:1fr 1fr;gap:1px 8px;font-size:7px;line-height:1.5;list-style:none;margin-bottom:14px}
  .services__contact{position:relative;font-size:8.6px;font-weight:700;line-height:1.35;text-align:center;margin-bottom:10px}
  .services__photo{position:relative;display:block;width:100px;height:86px;margin:0 auto 10px;background:linear-gradient(150deg,#9bb3c4,#5d7f99);border:3px solid #fff;box-shadow:0 1px 4px rgba(0,0,0,.25)}
  .services__details{position:relative;text-align:center;font-size:7.6px;font-weight:700;line-height:1.45}

  .panel--cover{background:linear-gradient(180deg,#eef6fb,var(--paper) 70%);font-family:"Open Sans",sans-serif}
  .cover__band{position:absolute;top:24px;left:10px;right:0;height:158px;background:linear-gradient(135deg,var(--deep),var(--mid));border-radius:4px 0 0 4px}
  .cover__title{position:absolute;top:40px;left:24px;right:12px;color:#fff;font-size:15px;font-weight:700;line-height:1.2;text-align:center}
  .cover__rule{position:absolute;top:102px;left:30px;right:20px;height:1px;background:#fff}
  .cover__tagline{position:absolute;top:196px;left:16px;right:12px;color:var(--deep);font-size:14px;font-weight:700;line-height:1.25;text-align:center}
  .brand{position:absolute;bottom:40px;left:0;right:0;display:flex;flex-direction:column;align-items:center;gap:6px;color:var(--mid);font-family:"Open Sans",sans-serif;font-weight:600}
  .brand__dot{width:22px;height:22px;border-radius:50%;background:var(--mid)}
  .brand__name{font-size:12px;letter-spacing:.08em;text-align:center;line-height:1.3}

  /* inside */
  .spread--inside .panel{font-family:"Tinos",serif;font-size:7px;line-height:1.45;padding:16px 12px}
  .panel--white{background:var(--paper);color:var(--ink)}
  .panel--blue{background:linear-gradient(180deg,var(--mid),var(--deep));color:#fff}
  .copy{position:relative}
  .copy p{margin-bottom:4px}
  .heading{font-family:"Tinos",serif;font-weight:700;font-size:11.5px;margin:2px 0 7px;color:var(--ink);padding-left:6px;border-left:3px solid var(--accent-red)}
  .heading--plain{border-left:none;padding-left:0;margin-top:10px}
  .heading--light{color:#fff;border-left:none;padding-left:0}
  .lead{font-size:7.4px;line-height:1.45;padding-left:6px;border-left:3px solid var(--accent-red);margin-bottom:6px}
  .footer-url{position:absolute;bottom:14px;left:0;right:0;text-align:center;font-size:6.5px;color:#fff}
</style>
</head>
<body>
<div class="canvas">

  <section class="spread spread--outside" aria-label="Brochure outside">
    <div class="panel panel--intro">
      <div class="water-area water-area--intro" role="img" aria-label="Soft decorative water swirl in light blue"></div>
      <h2 class="intro__title">Hypnosis can help you succeed when nothing else has worked!</h2>
      <div class="intro__text">
        <p>Many people come to us after trying diets, programs and willpower alone. Hypnosis works with the part of your mind that holds habits, so change can feel natural and lasting.</p>
        <p>Our certified hypnotherapists listen first, then build a plan around your goals. Sessions are calm, private and respectful, and you stay aware and in control the whole time.</p>
        <p>Whether you want to release stress, sleep better or move past old patterns, we are here to help you take the next step. It is part of our life.</p>
      </div>
    </div>

    <div class="panel panel--services">
      <div class="water-area water-area--services" role="img" aria-label="Soft decorative water swirl in pale blue"></div>
      <h2 class="services__title">Hypnosis can help you with the following and more:</h2>
      <ul class="services__list">
        <li>Stop Smoking</li><li>Health Issues</li>
        <li>Weight Loss</li><li>Self Esteem</li>
        <li>Stress Release</li><li>Concentration</li>
        <li>Fears, Phobias</li><li>Self-Confidence</li>
        <li>Habits</li><li>Test Anxiety</li>
        <li>Sleep Issues</li><li>Procrastination</li>
        <li>Public Speaking</li><li>Sports</li>
        <li>Pain Management</li><li>And More...</li>
      </ul>
      <p class="services__contact">Contact our office for more information. Your hypnotherapist will be happy to tell you about appointment availability and fees for services.</p>
      <div class="services__photo" role="img" aria-label="Portrait photograph of the hypnotherapist"></div>
      <p class="services__details">(555) 014-2290<br>HarborMistHypnosis.com<br>Copyright © 2014 Harbor Mist Hypnosis Center. All rights reserved.</p>
    </div>

    <div class="panel panel--cover">
      <div class="water-area water-area--cover" role="img" aria-label="Soft decorative water swirl in blue and sea green"></div>
      <div class="cover__band"></div>
      <h1 class="cover__title">Hypnosis and Hypnotherapy Information</h1>
      <div class="cover__rule"></div>
      <p class="cover__tagline">Learn how hypnosis and hypnotherapy can help you succeed.</p>
      <div class="brand">
        <span class="brand__dot"></span>
        <span class="brand__name">HARBOR MIST<br>HYPNOSIS CENTER</span>
      </div>
    </div>
  </section>

  <section class="spread spread--inside" aria-label="Brochure inside">
    <div class="panel panel--white">
      <div class="copy">
        <h2 class="heading">What is hypnosis?</h2>
        <p>Hypnosis is a state of focused consciousness. Your hypnotherapist will assist you in learning how to achieve this state by guiding you into it. Once this has been achieved, you will then receive what are called hypnotic suggestions. These suggestions will enable you to use the power of hypnosis in your life and make the changes you desire.</p>
        <p>Hypnosis is a tool that can help you just, like it has helped millions of other people to take back control of their lives.</p>
        <p>Hypnosis can help you change old habits and to provide you with motivation to do the things that you may have been putting off.</p>
        <p>Hypnosis has been sanctioned and used by the medical community since 1958 to help patients overcome chronic pain, create anesthesia, and heal psychogenic illnesses.</p>
        <p>Hypnosis and self-hypnosis have been shown to be effective in reducing stress and stress-related illnesses.</p>
        <h2 class="heading heading--plain">Is hypnosis safe?</h2>
        <p>Hypnosis is safe. It is very similar to experiencing a daydream. Usually you will feel relaxed when doing hypnosis. Hypnosis in and of itself is a very pleasant experience. It is a time to let go of the other thoughts of the day and focus on the issues you came in to work on.</p>
      </div>
    </div>

    <div class="panel panel--blue">
      <div class="copy">
        <p>Scientists, medical professionals, psychologists and hypnotherapists have been using hypnosis for over 200 years and no one has ever been hurt by simply going into hypnosis.</p>
        <h2 class="heading heading--light">What is hypnotherapy?</h2>
        <p>Hypnotherapy is the applied use of hypnosis. Therapy can be defined as anything that is done to move someone toward health and wholeness. Thus, hypnotherapy is the use of hypnosis to help you move toward health and wholeness.</p>
        <p>Hypnotherapy is also used to help you reach goals when nothing else has helped. See the back panel of this brochure to see a list of uses for hypnotherapy.</p>
        <p>Self-hypnosis may also be part of a good hypnotherapy program. Ask your hypnotherapist if using self-hypnosis is recommended to help you reach your goals.</p>
        <p>Can I be hypnotized?<br>Of course you can! You already have been. It's easy to go into hypnosis and it is a normal state of mind that everyone has already experienced.</p>
        <p>In fact, hypnosis is such a normal state of mind, most people usually don't even realize that they are hypnotized.</p>
        <p>Normal, everyday hypnosis occurs when you are driving down the road and lose track of time, or, when you are focusing on a book or television program and you don't even notice something that is going on around you.</p>
      </div>
      <p class="footer-url">www.HarborMistHypnosis.com</p>
    </div>

    <div class="panel panel--white">
      <div class="copy">
        <p class="lead">When you come in for hypnosis, all you need to do is to be able to follow the instructions of the hypnotherapist and you can put the power of hypnosis to work for you.</p>
        <p>Anyone of with the willingness and ability to follow instructions can experience hypnosis and use it to improve his or her life. This includes children and teenagers.</p>
        <p>Who will hypnotize me?</p>
        <p>Your hypnotist or hypnotherapist is a highly qualified professional. He or she is certified and registered with the Coastal Guild of Hypnotists.</p>
        <p>Your hypnotherapist is bound by professional ethics and the laws of the state in which it is practiced.</p>
        <p>In addition, your hypnotherapist has achieved extra certification in the advanced hypnotherapy system called TidePath. Rest assured that he or she will treat you with respect, and that your visits are completely confidential.</p>
        <p>We suggest that you call and speak to us directly so that you can learn more about hypnosis and hypnotherapy. This will allow you to become more familiar with our approach.</p>
      </div>
    </div>
  </section>

</div>
</body>
</html>
```